Analytics software company needs a business card design

We need a business card design for a global analytics software provider called 'Varnel Software'. Our main focus is developing real estate analysis software. We are open to any color scheme. The final design should be simple, modern, and precise.
Updates

There is one day left in our project and we are still looking forward to receiving additional submissions. We look forward to selecting one of your designs. Thanks.

Industry/Entity Type

Real Estate

```html
<!DOCTYPE html>
<html lang="en">
<head>
<meta charset="utf-8">
<title>Varnel Software — Business Card</title>
<link rel="stylesheet" href="https://fonts.googleapis.com/css2?family=Montserrat:wght@400;500;700&display=swap">
<style>
  :root {
    --backdrop: #0c0d0e;
    --card: #2a2c2e;
    --brand-blue: #3a84f0;
    --ink-soft: #3a84f0;
  }
  * { box-sizing: border-box; margin: 0; padding: 0; }
  html, body {
    width: 1200px;
    height: 817px;
    overflow: hidden;
    background: var(--backdrop);
    font-family: "Montserrat", sans-serif;
  }
  .sheet {
    width: 1200px;
    height: 817px;
    display: flex;
    align-items: center;
    justify-content: center;
    gap: 48px;
  }
  .card {
    position: relative;
    width: 540px;
    height: 309px;
    background: var(--card);
    color: var(--brand-blue);
  }
  /* Front: contact side */
  .contact {
    position: absolute;
    top: 28px;
    right: 30px;
    text-align: right;
    font-size: 11px;
    line-height: 1.45;
    font-weight: 400;
  }
  .contact .person {
    font-size: 17px;
    font-weight: 500;
    line-height: 1.2;
  }
  .contact .role { margin-bottom: 10px; }
  .contact .group { margin-bottom: 10px; }
  .wordmark-small {
    position: absolute;
    left: 30px;
    bottom: 30px;
    font-size: 22px;
    font-weight: 500;
    letter-spacing: 0.02em;
  }
  /* Back: brand side */
  .tagline {
    position: absolute;
    left: 30px;
    bottom: 34px;
    font-size: 20px;
    font-weight: 700;
    line-height: 1.05;
  }
  .wordmark-large {
    position: absolute;
    right: 30px;
    top: 40px;
    font-size: 34px;
    font-weight: 500;
    letter-spacing: 0.02em;
  }
</style>
</head>
<body>
  <main class="sheet">
    <section class="card card-front" aria-label="Business card front">
      <div class="contact">
        <p class="person">Elin Marsh</p>
        <p class="role">lorem ipsum</p>
        <div class="group">
          <p>555 xxx xxxx</p>
          <p>555 xxx xxxx</p>
        </div>
        <div class="group">
          <p>xx lorem ipsum street</p>
          <p>dolor sit amet</p>
        </div>
        <p>elin.marsh@varnelsoftware.com</p>
        <p>www.varnelsoftware.com</p>
        <p>@varnelsoftware</p>
      </div>
      <p class="wordmark-small">Varnel Software</p>
    </section>

    <section class="card card-back" aria-label="Business card back">
      <p class="wordmark-large">Varnel Software</p>
      <p class="tagline">Integrated<br>Technology</p>
    </section>
  </main>
</body>
</html>
```